Builders Worksite Corflute Outdoor Sign

We are a building company who are just branching out into new construction. How first new build is our own home which was designed by us and a local architect. We are proud and want to create more advertisement around our business.

We need a corflute sign that can staked outside the construction site and can be seen by people passing by.
Updates

Can we please make the company name and logo bigger (Tidewater Ridge Homes) This needs to be the focus. Can we please replace 'Manu' with 'Contact Us on 021-574-3619'

Target Market(s)

Home owners and people wishing to build on lifestyle blocks in New Zealand.

Font styles to use
Sans Serif

Requirements
Must have
• It needs to feature our:
Logo
Company name
Contact name and number - Manu - 0215743619
Landscape NOT portrait.

```html
<!DOCTYPE html>
<html lang="en">
<head>
<meta charset="utf-8">
<title>Tidewater Ridge Homes – Site Sign Options</title>
<link rel="stylesheet" href="https://fonts.googleapis.com/css2?family=Jost:wght@300;400&family=League+Spartan:wght@700&display=swap">
<style>
  :root {
    --board-grey: #8a8a8a;
    --navy: #1a202e;
    --gold: #f2c114;
    --gold-deep: #d19a2a;
    --white: #ffffff;
    --label: #f4f4f4;
  }
  * { margin: 0; padding: 0; box-sizing: border-box; }
  html, body { width: 848px; height: 1200px; overflow: hidden; }
  body { background: var(--board-grey); position: relative; font-family: "Jost", sans-serif; }

  .option-label {
    position: absolute; left: 60px;
    font: 300 12px/1 "Jost", sans-serif;
    letter-spacing: 2px; color: var(--label);
  }
  .option-label--one { top: 50px; }
  .option-label--two { top: 609px; }

  .sign {
    position: absolute; left: 60px; width: 708px; height: 500px;
    background: var(--gold);
    box-shadow: 0 1px 3px rgba(0,0,0,.25);
    overflow: hidden;
  }
  .sign--dark { top: 72px; }
  .sign--light { top: 634px; }

  .sign__panel { position: absolute; }
  .sign--dark .sign__panel { left: 10px; top: 12px; right: 9px; height: 399px; background: var(--navy); }
  .sign--light .sign__frame { position: absolute; left: 7px; top: 6px; right: 7px; bottom: 0; background: var(--navy); }
  .sign--light .sign__panel { left: 18px; top: 14px; right: 17px; bottom: 89px; background: var(--white); }

  .brand-dot {
    position: absolute; left: 298px; top: 100px; width: 112px; height: 112px;
    border-radius: 50%;
    background: linear-gradient(to bottom, var(--gold), var(--gold-deep));
  }
  .brand-name {
    position: absolute; left: 0; right: 0; top: 258px;
    text-align: center;
    font: 400 57px/70px "Jost", sans-serif;
    letter-spacing: 0.5px;
  }
  .brand-sub {
    position: absolute; left: 0; right: 0; top: 352px;
    text-align: center;
    font: 400 44px/48px "Jost", sans-serif;
    letter-spacing: 30px; padding-left: 30px;
  }
  .sign--dark .brand-name, .sign--dark .brand-sub { color: var(--white); }
  .sign--light .brand-name, .sign--light .brand-sub { color: var(--navy); }

  .contact-band {
    position: absolute; left: 0; right: 0; bottom: 0; height: 89px;
    display: flex; align-items: center; justify-content: center; gap: 16px;
    font-family: "League Spartan", sans-serif; font-weight: 700;
    padding-top: 6px;
  }
  .sign--light .contact-band { background: var(--navy); }
  .contact-band__lead { font-size: 40px; }
  .contact-band__number { font-size: 52px; letter-spacing: 1px; }
  .sign--dark .contact-band__lead, .sign--dark .contact-band__number { color: var(--navy); }
  .sign--light .contact-band__lead { color: var(--white); }
  .sign--light .contact-band__number { color: var(--gold); }
</style>
</head>
<body>
  <p class="option-label option-label--one">SAMPLE 1</p>
  <section class="sign sign--dark">
    <div class="sign__panel">
      <div class="brand-dot"></div>
    </div>
    <div class="brand-name">TIDEWATER RIDGE</div>
    <div class="brand-sub">HOMES</div>
    <div class="contact-band">
      <span class="contact-band__lead">Contact Us on</span>
      <span class="contact-band__number">021-574-3619</span>
    </div>
  </section>

  <p class="option-label option-label--two">SAMPLE 2</p>
  <section class="sign sign--light">
    <div class="sign__frame"></div>
    <div class="sign__panel">
      <div class="brand-dot" style="left:280px;top:86px;"></div>
    </div>
    <div class="brand-name">TIDEWATER RIDGE</div>
    <div class="brand-sub">HOMES</div>
    <div class="contact-band">
      <span class="contact-band__lead">Contact Us on</span>
      <span class="contact-band__number">021-574-3619</span>
    </div>
  </section>
</body>
</html>
```